Quellora business card design

create modern and tech looking business card that is clean but effectively communciates that we are a cloud communications company.
Should have at minimum:
Employee Name
Postion
Phone Number
Email
website
Contact Information for Business Card
create modern and tech looking business card that is clean but effectively communciates that we are a cloud communications company. We have two logo color schemes (attached) so would like to see designs both ways
Should have at minimum:
Employee Name
Postion
Phone Number
Email
website

```html
<!DOCTYPE html>
<html lang="en">
<head>
<meta charset="utf-8">
<title>Quellora business card</title>
<link href="https://fonts.googleapis.com/css2?family=Lato:wght@400;700&display=swap" rel="stylesheet">
<style>
  :root {
    --backdrop: #2b2b2b;
    --card-dark: #2e2e2e;
    --card-light: #f4f4f4;
    --ink: #3a3a3a;
    --ink-soft: #555555;
    --accent-cyan: #2fb8d6;
    --accent-green: #8cc63f;
    --brand-light: #ffffff;
  }
  * { box-sizing: border-box; margin: 0; padding: 0; }
  html, body {
    width: 1200px;
    height: 834px;
    overflow: hidden;
    background: var(--backdrop);
    font-family: "Lato", Arial, sans-serif;
  }
  .sheet {
    width: 1200px;
    height: 834px;
    display: flex;
    align-items: center;
    justify-content: center;
    gap: 40px;
  }
  .card {
    width: 560px;
    height: 320px;
    position: relative;
    box-shadow: 0 10px 30px rgba(0,0,0,.45);
  }
  .card--front {
    background: linear-gradient(135deg, #353535 0%, var(--card-dark) 60%, #262626 100%);
    display: flex;
    align-items: center;
    justify-content: center;
  }
  .card--back {
    background: linear-gradient(135deg, #ffffff 0%, var(--card-light) 60%, #e6e6e6 100%);
  }
  .brand {
    display: flex;
    align-items: center;
    gap: 12px;
    font-weight: 700;
    font-size: 34px;
    letter-spacing: 3px;
    text-transform: uppercase;
  }
  .brand__dot {
    width: 18px;
    height: 18px;
    border-radius: 50%;
    background: var(--accent-cyan);
  }
  .card--front .brand { color: var(--brand-light); }
  .card--back .brand {
    color: var(--ink);
    position: absolute;
    top: 78px;
    left: 50%;
    transform: translateX(-50%);
  }
  .person {
    position: absolute;
    left: 90px;
    bottom: 70px;
  }
  .person__name {
    font-size: 20px;
    font-weight: 700;
    color: var(--ink);
  }
  .person__role {
    font-size: 15px;
    color: var(--accent-green);
    margin-top: 2px;
  }
  .contacts {
    position: absolute;
    left: 310px;
    bottom: 62px;
    list-style: none;
  }
  .contacts__item {
    display: flex;
    align-items: center;
    gap: 12px;
    font-size: 14px;
    color: var(--ink-soft);
    line-height: 26px;
  }
  .contacts__icon {
    width: 16px;
    height: 16px;
    flex: none;
  }
</style>
</head>
<body>
<main class="sheet">
  <section class="card card--front" aria-label="Card front">
    <div class="brand"><span class="brand__dot"></span>Quellora</div>
  </section>

  <section class="card card--back" aria-label="Card back">
    <div class="brand"><span class="brand__dot"></span>Quellora</div>

    <div class="person">
      <p class="person__name">Marek Lund</p>
      <p class="person__role">President</p>
    </div>

    <ul class="contacts">
      <li class="contacts__item">
        <svg class="contacts__icon" viewBox="0 0 16 16" fill="none" stroke="var(--accent-cyan)" stroke-width="1.4" stroke-linecap="round" stroke-linejoin="round">
          <path d="M3 2h3l1.2 3-1.7 1.2a8 8 0 0 0 4.3 4.3L11 8.8l3 1.2v3a1.5 1.5 0 0 1-1.6 1.5A12 12 0 0 1 1.5 3.6 1.5 1.5 0 0 1 3 2z"/>
        </svg>
        5550 104 208
      </li>
      <li class="contacts__item">
        <svg class="contacts__icon" viewBox="0 0 16 16" fill="none" stroke="var(--accent-cyan)" stroke-width="1.4" stroke-linejoin="round">
          <rect x="1.5" y="3.5" width="13" height="9"/>
          <path d="M1.5 3.5 8 9l6.5-5.5"/>
        </svg>
        email@quellora.com
      </li>
      <li class="contacts__item">
        <svg class="contacts__icon" viewBox="0 0 16 16" fill="none" stroke="var(--accent-cyan)" stroke-width="1.3">
          <circle cx="8" cy="8" r="6.5"/>
          <ellipse cx="8" cy="8" rx="2.8" ry="6.5"/>
          <path d="M1.5 8h13M2.5 4.8h11M2.5 11.2h11"/>
        </svg>
        www.quellora.com
      </li>
    </ul>
  </section>
</main>
</body>
</html>
```